Veltrano Community Development Planning New web site

Design a new web site. I have a budget of $1,500.00.
Attached on PowerPoint is a complete site plan. Home page and linked pages.
10 - 12 pages. All copy and photos will be supplied. (300dpi)
I have shown them the concept which they like.
No data bases required. Home page with animations dissolving.
They former web site has been taken down. They have been in business 30 years in New Jersey
Colors teal blues and greens
There will be a new logo)being designed)
The text in home page copy will give you a detailed story what they are all about.

files have been approved for Veltrano, Inc.   Tomas is the designer

Industry/Entity Type

Community

```html
<!DOCTYPE html>
<html lang="en">
<head>
<meta charset="utf-8">
<title>veltranoinc.org</title>
<link href="https://fonts.googleapis.com/css2?family=Source+Sans+3:ital,wght@0,400;0,600;0,700;1,400;1,700&display=swap" rel="stylesheet">
<style>
:root{
  --teal:#1aa39a;
  --teal-dark:#14897f;
  --ink:#333;
  --muted:#555;
  --panel:#ededed;
  --field:#e9e9e9;
  --footer:#2e2e2e;
  --white:#fff;
}
*{margin:0;padding:0;box-sizing:border-box}
html,body{width:878px;height:1200px;overflow:hidden;background:var(--white)}
body{position:relative;font-family:"Source Sans 3",sans-serif;color:var(--ink)}
.abs{position:absolute}
.topbar{left:0;top:0;width:878px;height:4px;background:var(--teal)}
.brand{left:144px;top:27px;display:flex;align-items:center;gap:7px;font-size:16px;font-weight:600;color:#555}
.brand-dot{width:30px;height:30px;border-radius:50%;background:var(--teal)}
.nav{left:330px;top:36px;display:flex;gap:15px;font-size:8.5px;align-items:center}
.nav a{color:#222;text-decoration:none}
.nav a.active{background:var(--teal);color:#fff;padding:3px 5px;border-radius:2px}
.hero{left:0;top:77px;width:878px;height:299px;background:linear-gradient(90deg,#dfe3e6 0%,#cfd6db 40%,#8d99a3 62%,#5d6a78 80%,#44505d 100%)}
.hero-title{left:128px;top:166px;font-size:26px;color:#111;letter-spacing:-.3px}
.hero-text{left:130px;top:209px;width:255px;font-size:7.6px;line-height:13.6px;color:#222}
.btn{background:var(--teal);color:#fff;display:flex;align-items:center;justify-content:center;border-radius:2px}
.hero-btn{left:130px;top:282px;width:87px;height:28px;font-size:9.5px}
.dots{left:412px;top:389px;display:flex;gap:3px}
.dots i{width:6px;height:6px;border-radius:50%;background:#d7dcdc}
.dots i.on{background:var(--teal)}
.h-teal{color:var(--teal);font-weight:700}
.welcome-h{left:144px;top:406px;font-size:12.5px;font-weight:600}
.photo{background:linear-gradient(135deg,#8e9aa3,#c7a53a 55%,#4e555c)}
.welcome-img{left:144px;top:441px;width:102px;height:67px}
.body-text{font-size:6.9px;line-height:11.2px;color:#333;text-align:justify}
.welcome-text{left:271px;top:440px;width:462px}
.subscribe{left:144px;top:548px;width:590px;height:54px;background:var(--panel)}
.sub-label{left:198px;top:569px;font-size:8px;color:#444}
.sub-input{left:333px;top:562px;width:185px;height:24px;background:#fff;font-size:8px;color:#777;padding:7px 10px}
.sub-btn{left:558px;top:559px;width:96px;height:31px;font-size:13px;font-style:italic;font-weight:700}
.sec-h{font-size:12px;font-weight:700}
.icon{fill:#b9b9b9}
.list{left:526px;top:733px;font-size:7px;line-height:11.2px;list-style:none}
.list li::before{content:"";display:inline-block;width:2px;height:2px;background:var(--teal);margin:0 9px 1.5px -12px}
.more{font-size:7px;letter-spacing:.3px;display:flex;align-items:center;gap:6px;color:#222}
.divider{left:144px;top:846px;width:590px;height:11px;background:repeating-linear-gradient(135deg,#d8d8d8 0 1px,#fff 1px 3px)}
.quote{left:144px;top:934px;width:176px;height:90px;background:var(--panel);padding:9px 7px;font-size:7.8px;font-style:italic;line-height:12.6px;color:#555;text-align:justify}
.quote-tail{left:154px;top:1024px;width:0;height:0;border-left:8px solid var(--panel);border-bottom:8px solid transparent}
.quote-by{left:157px;top:1042px;font-size:8.5px;font-style:italic;color:var(--teal)}
.quote-by small{font-size:6.8px;color:#555}
.post{left:346px;width:194px;background:var(--panel);display:flex;gap:10px;padding:6px 8px 6px 3px}
.post-thumb{width:40px;height:40px;border-radius:50%;flex:none;border:2px solid #fff;background:linear-gradient(135deg,#c9a531,#4b6a89)}
.post p{font-size:6.8px;line-height:11.2px;color:#333}
.field{left:563px;width:170px;background:var(--field);font-size:7px;color:#777;padding:6px 10px}
.send{left:651px;top:1060px;width:82px;height:26px;font-size:9px}
.footer{left:0;top:1128px;width:878px;height:72px;background:var(--footer)}
.foot-links{left:142px;top:1146px;font-size:7px;color:#fff}
.foot-links span{margin:0 4px;color:#ccc}
.copy{left:142px;top:1167px;font-size:7px;color:#fff}
.social{left:628px;top:1155px;display:flex;gap:12px}
.social i{width:11px;height:11px;border-radius:50%;background:#d0d0d0}
</style>
</head>
<body>
<div class="abs topbar"></div>

<div class="abs brand"><span class="brand-dot"></span>veltranoinc.org</div>
<nav class="abs nav">
  <a class="active" href="#">Home</a><a href="#">Our Company</a><a href="#">Services</a><a href="#">Housing Rehab Application</a><a href="#">Affordable Application</a><a href="#">Contact Us</a>
</nav>

<section class="abs hero" role="img" aria-label="Two engineers in hard hats at a construction site, one pointing upward"></section>
<h1 class="abs hero-title">VELTRANOINC.ORG</h1>
<p class="abs hero-text">Consectetur adipiscing elit. Vivamus non diam et lacus pulvinar venenatis et vestibulum velit. Pellentesque interdum faucibus dui hendrerit ultrices. Aliquam erat volutpat. Duis commodo turpis id diam pulvinar hendrerit turpis id diam pulvinar hendrerit.</p>
<a class="abs btn hero-btn">READ MORE</a>
<div class="abs dots"><i class="on"></i><i></i><i></i><i></i></div>

<h2 class="abs welcome-h h-teal">Welcome to veltranoinc.org</h2>
<div class="abs welcome-img photo" role="img" aria-label="Worker holding a yellow hard hat near a building under construction"></div>
<p class="abs body-text welcome-text">Veltrano, Inc. is a city planning firm that specializes in community development and housingrehabilitation program planning, design and implementation. We have over twenty years of experience in developing and administering income-based housing programs in accordance with US Department of Housing and Urban Development (HUD) and New Jersey Council on Affordable Housing (COAH) rules and regulations. In addition, our firm is capable of providing the technical and administrative assistance our clients require for the implementation of their income-based housing programs. Veltrano's sister company, Harlan Mercer Associates, is one of the most experienced urban planning firms in New Jersey, with over forty years as consulting planners.</p>

<div class="abs subscribe"></div>
<div class="abs sub-label">Subscribe to our mailing list</div>
<div class="abs sub-input">Email</div>
<a class="abs btn sub-btn">Subscribe</a>

<svg class="abs icon" style="left:146px;top:626px" width="34" height="26" viewBox="0 0 34 26"><circle cx="19" cy="8" r="7"/><path d="M6 26c0-8 6-11 13-11s13 3 13 11z"/><circle cx="10" cy="9" r="5" opacity=".7"/><path d="M0 25c0-6 4-9 9-9h2c-3 2-5 5-5 9z" opacity=".7"/></svg>
<h3 class="abs sec-h h-teal" style="left:194px;top:633px">Our Company</h3>
<svg class="abs icon" style="left:436px;top:626px" width="28" height="28" viewBox="0 0 28 28"><path d="M12 0h4l1 4 3 1.3 3.5-2.2 2.8 2.8-2.2 3.5L25.4 12l4 1v4l-4 1-1.3 3 2.2 3.5-2.8 2.8-3.5-2.2-3 1.3-1 4h-4l-1-4-3-1.3-3.5 2.2-2.8-2.8 2.2-3.5L2.6 17l-4-1v-4l4-1 1.3-3-2.2-3.5 2.8-2.8 3.5 2.2L11 4zM14 9a5 5 0 100 10 5 5 0 000-10z"/></svg>
<h3 class="abs sec-h h-teal" style="left:483px;top:633px">Services</h3>

<div class="abs body-text" style="left:146px;top:678px;width:246px">
  <p>Veltrano, Inc stands for Community, Grants, Planning and Housing. We specialize in all aspects of affordable housing, planning, COAH compliance, and the procurement of grants and loans for our clients.</p>
  <p style="margin-top:11.2px">Founded in 1975, Veltrano has grown to be the only full service affordable housing implementation company in New Jersey. Seasoned in all facets of community development, Veltrano boasts a team that includes professional planners, expert grant-writers, COAH certified housing specialists, licensed building inspectors, lead testers, and knowledgeable support staff. Client needs are promptly met with continuity,</p>
</div>
<div class="abs photo" style="left:433px;top:681px;width:65px;height:56px;background:linear-gradient(160deg,#7aa3c9,#c7b89a 60%,#6b5a4a)" role="img" aria-label="Family in front of a drawn house outline"></div>
<p class="abs body-text" style="left:514px;top:678px;width:206px">Our full scope of services includes assisting civic, government organizations and private development firms with strategic thinking, planning, funding solutions, implementation and management of projects including:</p>
<ul class="abs list">
  <li>Housing and Relocation</li><li>Housing Development</li><li>Relocation</li><li>COAH Compliance</li><li>Property Acquisition</li>
</ul>

<div class="abs more" style="left:149px;top:810px"><svg width="10" height="7" viewBox="0 0 10 7"><path d="M0 0l3.5 3.5L0 7M5 0l3.5 3.5L5 7" fill="none" stroke="#222" stroke-width="1.6"/></svg>FIND OUT MORE</div>
<div class="abs more" style="left:437px;top:809px"><svg width="10" height="7" viewBox="0 0 10 7"><path d="M0 0l3.5 3.5L0 7M5 0l3.5 3.5L5 7" fill="none" stroke="#222" stroke-width="1.6"/></svg>FIND OUT MORE</div>

<div class="abs divider"></div>

<svg class="abs icon" style="left:149px;top:886px" width="27" height="26" viewBox="0 0 27 26"><path d="M0 0h27v20H10l-6 6v-6H0z"/><path d="M4 5h19M4 9h19M4 13h19" stroke="#fff" stroke-width="1"/></svg>
<h3 class="abs sec-h h-teal" style="left:186px;top:889px">Client Stories</h3>
<svg class="abs" style="left:347px;top:882px" width="30" height="26" viewBox="0 0 30 26"><rect x="2" y="4" width="20" height="16" fill="#c5c5c5" transform="rotate(-12 12 12)"/><path d="M8 20L28 2" stroke="#444" stroke-width="2"/><path d="M0 23h30" stroke="#888" stroke-width="1"/></svg>
<h3 class="abs sec-h h-teal" style="left:390px;top:889px">Blog</h3>
<svg class="abs icon" style="left:567px;top:886px" width="27" height="22" viewBox="0 0 27 22"><rect y="3" width="27" height="19" rx="1"/><rect x="10" width="7" height="5" fill="#999"/><circle cx="7" cy="11" r="3" fill="#fff"/><path d="M2 19c0-3 2-5 5-5s5 2 5 5z" fill="#fff"/><path d="M15 10h9M15 13h9M15 16h7" stroke="#fff"/></svg>
<h3 class="abs sec-h h-teal" style="left:610px;top:890px">Contact Me</h3>

<blockquote class="abs quote">In ac ipsum urna. Nunc condimentum est nec lorem ultrices commodo. Aenean pharetra sapien sed nisl sodales sagittis. Donec eget metus vel nibh pharetra euismod sit amet vel nulla.</blockquote>
<div class="abs quote-tail"></div>
<div class="abs quote-by">Marta Kessel <small>Wedding Planners</small></div>

<article class="abs post" style="top:933px"><div class="post-thumb" role="img" aria-label="Workers in hard hats reviewing plans"></div><p>In ultricies pellentesque massa a porta. Aliquam ipsum enim, hendrerit ut porta nec. ullamcorper et nulla. In eget mi dui, sit amet.</p></article>
<article class="abs post" style="top:995px"><div class="post-thumb" role="img" aria-label="Engineers discussing a project"></div><p>In ultricies pellentesque massa a porta. Aliquam ipsum enim, hendrerit ut porta nec. ullamcorper et nulla. In eget mi dui, sit amet.</p></article>

<div class="abs field" style="top:933px;height:21px">Your Name</div>
<div class="abs field" style="top:960px;height:20px">Your Email</div>
<div class="abs field" style="top:986px;height:64px">Your Message</div>
<a class="abs btn send">Send Message</a>

<div class="abs more" style="left:147px;top:1073px"><svg width="10" height="7" viewBox="0 0 10 7"><path d="M0 0l3.5 3.5L0 7M5 0l3.5 3.5L5 7" fill="none" stroke="#222" stroke-width="1.6"/></svg>FIND OUT MORE</div>
<div class="abs more" style="left:348px;top:1073px"><svg width="10" height="7" viewBox="0 0 10 7"><path d="M0 0l3.5 3.5L0 7M5 0l3.5 3.5L5 7" fill="none" stroke="#222" stroke-width="1.6"/></svg>FIND OUT MORE</div>

<footer class="abs footer"></footer>
<div class="abs foot-links">Home<span>|</span>Our Company<span>|</span>Services<span>|</span>Housing Rehab Application<span>|</span>Affordable Application<span>|</span>Contact Us</div>
<div class="abs copy">© Copyright 2014 veltranoinc.org. All rights reserved.</div>
<div class="abs social" aria-label="Social links"><i></i><i></i><i></i><i></i><i></i></div>
</body>
</html>
```